An international recruitment business looking to attract new engineering and construction clients i

VK Globalis is an international recruitment company with a wealth of experienced engineers, quantity surveyors and construction specialists appropriate to fill roles in the vastly growing Middle East. We need a new, attractive brochure design to send to new clients/companies so they will be interested in our recruitment company and our candidates. We have provided our company logo which we would like to feature, and we would like the theme to match this to some extent. We have also attached our current brochure which should be used for the general content and information. PLEASE NOTE: Ignore the appraisals on the penultimate page - I will provide new ones in a separate document. (Use the one with 5 appraisals, not 3!)
The final design should be modern and attractive and should feature some images of the Middle East including some impressive buildings and new railways (similar to our current ones).
Please also link our website
and use it for inspiration: http://www.vk-globalis.co.uk
Updates
We would like the brochure to be A5 and landscape - although it will only be emailed to clients and not printed.
There is no limit on number of pages.
There seems to be a problem opening the appraisals document I attached.
The content of this document is:
VK Globalis Appraisals
"I had the pleasure of working with VK Globalis as a client and found them to be a great recruiter with in-depth rail knowledge, I had great results from them time after time. I found the team very trustworthy, professional and fun to work with. I would highly recommend VK Globalis and will continue to use the company for all my future recruitment needs"
Tarek Belvedoni, Harbel Transit Company
“When looking to advance my career, I enquired with VK Globalis about a senior position in the Middle East. I dealt specifically with Morven who I found very helpful. He informed me of all the job requirements, the background of the role, responsibilities and package. Morven was extremely diligent in moving the process forward and throughout kept in contact and abreast of the situation. In all it proved a great success and I am now happily placed in my new role. Even though Morven performed beyond the normal boundaries of his role he even now keeps in contact to make sure everything is ok and all parties happy and satisfied with the outcome. I wholeheartedly endorse Morven and VK Globalis and will use them when I am next supplementing my team.”
Ellis Thornbury, Head of Quantity Surveying, Orvane Delta Design Engineers (ODDE), Kuwait
VK Globalis is a recruitment company that has an insatiable appetite for understanding the jobs, for which they recruit, and not only the jobs, but they also establish excellent rapport with the clients and candidates. They are always there when I need to fill positions in my organization quickly. They listen to what I need and always supply me with the resumes that I could review right away to start hiring who I needed - saving me time and effort. They are always able to supply me with the exact person that I need for the open position."
Leila Haddou, HR Consultant, Harbel Lines
Target Market(s)
Professional clients in the Middle East
Industry/Entity Type
Construction
Colors
Designer to choose colors to be used in the design.
Look and feel

```html
<!DOCTYPE html>
<html lang="en">
<head>
<meta charset="utf-8">
<title>Expertise</title>
<link rel="stylesheet" href="https://fonts.googleapis.com/css2?family=EB+Garamond&family=Hind:wght@400&display=swap">
<style>
  :root {
    --page: #ffffff;
    --ink: #2b2b2b;
    --teal: #33b8a5;
    --ring: #e9e9e9;
    --band-text: #ffffff;
    --sky-top: #a9c6e0;
    --sky-low: #cbdbe8;
    --site-mid: #b9a895;
    --site-low: #5e5650;
  }
  * { margin: 0; padding: 0; box-sizing: border-box; }
  html, body { width: 1200px; height: 846px; overflow: hidden; background: var(--page); }
  .page { position: relative; width: 1200px; height: 846px; background: var(--page); }
  .hero { position: absolute; left: 0; top: 0; width: 1200px; height: 846px; }
  .section-title {
    position: absolute; left: 44px; top: 395px;
    font-family: "EB Garamond", Georgia, serif;
    font-size: 37px; font-weight: 400; color: var(--band-text); letter-spacing: 0.2px;
  }
  .intro {
    position: absolute; left: 668px; top: 38px; width: 487px;
    font-family: "Hind", Arial, sans-serif;
    font-size: 18.4px; line-height: 20.2px; color: var(--ink);
  }
  .intro p { margin-bottom: 20.2px; }
  .intro .line {
    display: block; white-space: nowrap;
    text-align: justify; text-align-last: justify;
  }
  .intro .line.end { text-align: left; text-align-last: left; }
</style>
</head>
<body>
<main class="page">
  <svg class="hero" width="1200" height="846" viewBox="0 0 1200 846">
    <defs>
      <clipPath id="lens">
        <circle cx="106" cy="423" r="496"/>
      </clipPath>
      <linearGradient id="skyline" x1="0" y1="0" x2="0" y2="1">
        <stop offset="0" stop-color="var(--sky-top)"/>
        <stop offset="0.55" stop-color="var(--sky-low)"/>
        <stop offset="0.78" stop-color="var(--site-mid)"/>
        <stop offset="1" stop-color="var(--site-low)"/>
      </linearGradient>
    </defs>
    <circle class="lens-ring" cx="106" cy="423" r="514" fill="var(--ring)"/>
    <g clip-path="url(#lens)">
      <rect class="lens-photo" x="0" y="0" width="640" height="846" fill="url(#skyline)"
            role="img" aria-label="Photograph of a supertall skyscraper rising above a construction site with tower cranes in the Middle East"/>
      <rect class="title-band" x="0" y="365" width="640" height="116" fill="var(--teal)"/>
    </g>
  </svg>

  <h2 class="section-title">Expertise</h2>

  <section class="intro">
    <p>
      <span class="line">As a consultancy we pride ourselves in taking full</span>
      <span class="line">responsibility for providing our clients with the very best</span>
      <span class="line end">selection of professionals from across the globe.</span>
    </p>
    <p>
      <span class="line">We currently recruit Construction &amp; Engineering</span>
      <span class="line">Professionals from the UK, EU, Australia, New Zealand,</span>
      <span class="line">Canada &amp; the USA to work with our prestigious clients</span>
      <span class="line end">across the Middle East.</span>
    </p>
    <p>
      <span class="line">Our company prides itself on taking the time and effort</span>
      <span class="line">involved in understanding our clients, their needs, their</span>
      <span class="line">past and most importantly the future of the company</span>
      <span class="line">and the direction it wishes to take. This information, in</span>
      <span class="line">turn provides us with the specifications we need to find</span>
      <span class="line end">the talent required for the future of your business.</span>
    </p>
    <p>
      <span class="line">We believe that research is a vital part of keeping ahead.</span>
      <span class="line">We therefore dedicate part of our business to the</span>
      <span class="line">continued study of Recruitment Trends, New</span>
      <span class="line">Developments &amp; Economic Pressures that can have a</span>
      <span class="line">major effect on where to find and source the best talent</span>
      <span class="line end">needed for you.</span>
    </p>
  </section>
</main>
</body>
</html>
```